BRIGHTWAY MOTOR DEALS
BRIGHTWAY MOTOR DEALS -
Creative Brief
Professional
DEAN VARLOW
SALES REP
742 N.CORVAL AVE HAMILTON OHIO 45019
BRIGHTWAYMOTORDEALS@QUILLMAIL.EXAMPLE
WWW.TORVENCARHOUSE.EXAMPLE

```html
<!DOCTYPE html>
<html lang="en">
<head>
<meta charset="utf-8">
<title>Brightway Motor Deals – Business Card</title>
<link rel="stylesheet" href="https://fonts.googleapis.com/css2?family=PT+Sans:wght@400;700&display=swap">
<style>
  :root {
    --backdrop: #3a3a3a;
    --card: #ffffff;
    --magenta: #b0207e;
    --magenta-light: #d0459d;
    --green: #8cc63f;
    --ink: #4a4a4a;
    --divider: #d9d9d9;
    --white: #ffffff;
  }
  html, body {
    margin: 0;
    padding: 0;
    width: 1200px;
    height: 780px;
    overflow: hidden;
    background: var(--backdrop);
    font-family: "PT Sans", Arial, sans-serif;
  }
  .card {
    position: absolute;
    left: 100px;
    top: 90px;
    width: 1000px;
    height: 600px;
    background: var(--card);
    border-radius: 34px;
    overflow: hidden;
  }
  .card-swoosh {
    position: absolute;
    left: 0;
    top: 0;
    width: 1000px;
    height: 600px;
  }
  .brand {
    position: absolute;
    left: 40px;
    top: 220px;
    width: 320px;
    display: flex;
    align-items: center;
    gap: 14px;
  }
  .brand-dot {
    width: 34px;
    height: 34px;
    border-radius: 50%;
    background: var(--magenta);
    flex: none;
  }
  .brand-name {
    color: var(--magenta);
    font-weight: 700;
    font-size: 34px;
    line-height: 1.05;
    letter-spacing: 0.5px;
  }
  .divider {
    position: absolute;
    left: 385px;
    top: 60px;
    width: 2px;
    height: 360px;
    background: var(--divider);
  }
  .contact {
    position: absolute;
    left: 460px;
    top: 82px;
    color: var(--ink);
    font-size: 25px;
    line-height: 1.3;
  }
  .address { margin: 0 0 44px; }
  .contact-line {
    display: flex;
    align-items: center;
    gap: 14px;
    margin-bottom: 8px;
  }
  .contact-icon {
    width: 24px;
    height: 24px;
    flex: none;
    color: var(--magenta);
    font-weight: 700;
    font-size: 26px;
    line-height: 24px;
    text-align: center;
  }
  .person {
    position: absolute;
    right: 56px;
    top: 410px;
    text-align: right;
    color: var(--white);
  }
  .person-name {
    font-weight: 700;
    font-size: 38px;
    margin: 0;
  }
  .person-title {
    font-size: 25px;
    margin: 2px 0 0;
  }
</style>
</head>
<body>
  <div class="card">
    <svg class="card-swoosh" viewBox="0 0 1000 600" aria-hidden="true">
      <path d="M0 510 C 300 560, 700 470, 1000 320 L1000 600 L0 600 Z" fill="var(--magenta)"/>
      <path d="M0 540 C 320 585, 700 510, 1000 380 L1000 600 L0 600 Z" fill="var(--magenta-light)" opacity="0.35"/>
      <path d="M260 520 C 560 500, 800 420, 1000 300" fill="none" stroke="var(--green)" stroke-width="5"/>
    </svg>

    <div class="brand">
      <span class="brand-dot"></span>
      <span class="brand-name">BRIGHTWAY<br>MOTOR DEALS</span>
    </div>

    <div class="divider"></div>

    <div class="contact">
      <p class="address">742 N.Corval Ave<br>Hamilton Ohio 45019</p>
      <div class="contact-line">
        <svg class="contact-icon" viewBox="0 0 24 24" aria-hidden="true">
          <path d="M6 2 L10 6 L8 9 C9 12 12 15 15 16 L18 14 L22 18 L19 22 C10 21 3 14 2 5 Z" fill="currentColor"/>
        </svg>
        <span>513-555-2840</span>
      </div>
      <div class="contact-line">
        <svg class="contact-icon" viewBox="0 0 24 24" aria-hidden="true">
          <rect x="6" y="2" width="12" height="7" fill="currentColor"/>
          <rect x="2" y="10" width="20" height="9" rx="2" fill="currentColor"/>
          <rect x="6" y="16" width="12" height="6" fill="currentColor"/>
        </svg>
        <span>513-555-2841</span>
      </div>
      <div class="contact-line">
        <span class="contact-icon">@</span>
        <span>brightwaymotordeals@quillmail.example</span>
      </div>
    </div>

    <div class="person">
      <p class="person-name">Dean Varlow</p>
      <p class="person-title">Sales rep</p>
    </div>
  </div>
</body>
</html>
```